Postcard - Promoting Wendell Ridge Brokers for Farm Clients

We need to develop a postcard (4" X 6") to send out to Agricultural clients.

The content on the email will be:

We understand that farming has variety of risk exposures that can affect your farm and your family’s future.
Wendell Ridge Brokers can help you identify and manage those risks by building an insurance program that works for you, your family and your operation. We ensure we understand your risk, you understand your coverage and we sort through the “fine” print together before a loss happens.
Contact Wendell Ridge Brokers to arrange a review and meet our team. 1-800-555-0147 farmteam@wendellridge.ca

Target Market(s)

We would like 2 separate postcards - one for crop farmers and one for cattle farmers

Industry/Entity Type

Agriculture

Requirements
Must have
• Be remarkable - something that catches your eye, and must have our logo

Please note that this can be 2 sided - potential to have the photo/color side to be the picture and some wording to catch the attention of the individual receiving .... and the back side to be the additional content, which is in the project description.

```html
<!DOCTYPE html>
<html lang="en">
<head>
<meta charset="utf-8">
<title>Wendell Ridge Brokers – Farm Postcard</title>
<link rel="stylesheet" href="https://fonts.googleapis.com/css2?family=Jost:wght@400&display=swap">
<style>
  :root {
    --navy: #233e8b;
    --cyan: #1bbdeb;
    --teal: #1f8fb3;
    --white: #ffffff;
    --photo-light: #eceaec;
    --photo-mid: #a8806f;
    --photo-dark: #4a3029;
    --grass: #5e7a3a;
  }
  html, body {
    margin: 0;
    padding: 0;
    overflow: hidden;
    background: #e9e9e9;
  }
  .postcard {
    position: relative;
    width: 1200px;
    height: 801px;
    background: var(--navy);
    overflow: hidden;
    font-family: "Jost", "Futura", sans-serif;
    color: var(--white);
  }
  .backdrop {
    position: absolute;
    inset: 0;
  }
  .brand {
    position: absolute;
    left: 24px;
    top: 48px;
    display: flex;
    align-items: center;
    gap: 12px;
  }
  .brand-mark {
    width: 44px;
    height: 44px;
    border-radius: 50%;
    border: 0;
    background: var(--white);
  }
  .brand-name {
    font-size: 25px;
    font-weight: 400;
    letter-spacing: 0.5px;
    line-height: 1.1;
    text-transform: uppercase;
  }
  .intro, .call-to-action {
    position: absolute;
    left: 37px;
    margin: 0;
    font-size: 20.5px;
    line-height: 26.7px;
    letter-spacing: 0.3px;
    white-space: nowrap;
  }
  .intro { top: 188px; }
  .call-to-action { top: 571px; }
  .contact-list {
    position: absolute;
    left: 42px;
    top: 677px;
    margin: 0;
    padding: 0;
    list-style: none;
    font-size: 20.5px;
  }
  .contact-item {
    display: flex;
    align-items: center;
    gap: 13px;
    height: 30px;
    margin-bottom: 15px;
  }
  .contact-icon {
    width: 28px;
    height: 28px;
    flex: none;
  }
</style>
</head>
<body>
<div class="postcard">
  <svg class="backdrop" width="1200" height="801" viewBox="0 0 1200 801">
    <defs>
      <linearGradient id="pasture" x1="0" y1="0" x2="1" y2="1">
        <stop offset="0" stop-color="var(--photo-light)"/>
        <stop offset="0.35" stop-color="#d9cfcd"/>
        <stop offset="0.6" stop-color="var(--photo-mid)"/>
        <stop offset="0.85" stop-color="var(--photo-dark)"/>
        <stop offset="1" stop-color="var(--grass)"/>
      </linearGradient>
    </defs>
    <path class="accent-band" d="M287,0 C310,150 350,260 440,390 C600,610 850,760 1200,805 L1200,0 Z" fill="var(--cyan)"/>
    <path class="accent-band-lower" d="M600,590 C760,700 950,770 1200,805 L1200,790 C960,760 780,690 620,590 Z" fill="var(--teal)"/>
    <path class="photo-area" role="img" aria-label="Photo of curious cattle crowding close in a sunlit pasture" d="M407,0 C330,110 330,230 420,360 C560,560 800,710 1200,782 L1200,0 Z" fill="url(#pasture)"/>
  </svg>

  <div class="brand">
    <span class="brand-mark"></span>
    <span class="brand-name">Wendell Ridge Brokers</span>
  </div>

  <p class="intro">We understand that farming<br>has variety of risk exposures<br>that can affect your farm and<br>your family’s future.<br>Wendell Ridge Brokers can help you<br>identify and manage those risks by<br>building an insurance program<br>that works for you, your family and<br>your operation. We ensure we understand<br>your risk, you understand your coverage and<br>we sort through the “fine” print together before<br>a loss happens.</p>

  <p class="call-to-action">Contact Wendell Ridge Brokers<br>to arrange a review and<br>meet our team.</p>

  <ul class="contact-list">
    <li class="contact-item">
      <svg class="contact-icon" viewBox="0 0 28 28" aria-hidden="true">
        <rect x="1" y="6" width="26" height="17" fill="var(--white)"/>
        <path d="M2,7 L14,16 L26,7 M2,22 L11,14 M26,22 L17,14" stroke="var(--navy)" stroke-width="1.8" fill="none"/>
      </svg>
      <span>farmteam@wendellridge.ca</span>
    </li>
    <li class="contact-item">
      <svg class="contact-icon" viewBox="0 0 28 28" aria-hidden="true">
        <path d="M6,2 L10,2 L13,9 L10,12 C11.5,16 13,17.5 17,19 L20,16 L27,19 L27,23 C27,25 25,27 23,27 C12,26 2,16 1,6 C1,4 3,2 6,2 Z" fill="var(--white)"/>
      </svg>
      <span>1-800-555-0147</span>
    </li>
  </ul>
</div>
</body>
</html>
```